A4 Childcare Spring Special Flyer

Ferngate Skills Academy is a registered training organisation (RTO) Toid No. 47318, based in Blackburn, Victoria. We are a market leader in Professional development courses both accredited and non accredited, in order for you to maintain currency in your profession.

We need a flyer for a childcare specific spring special. The special is to offer a $50 LUMBO gift card and 50% of your second training session. Conditions apply*

The training sessions available are the NEW childcare specific course: HLTAID004 Provide an emergency first aid response in an education and care setting and HLTAID003 Provide First Aid, HLTAID001 Provide Cardiopulmonary Resuscitation (CPR), 22024VIC Course in emergency management of asthma in the workplace
and 22099VIC Course in First Aid Management of Anaphylaxis.
We provide a flexible, cost effective and reliable service.
We have training locations available in Blackburn, Preston, Narre Warren and Mornington and can also provide onsite training.

We can also provide education and QERSOB regulation consultation to the childcare provider.

Must use company logo, include phone number: (03) 5550 1274, website: www.ferngateskillsacademy.com.au, email: maraflint@ferngateskillsacademy.com.au

(Note that a letter with more detail will be attached with this flyer, therefore, with that in mind; use that information as desired).

The final product should be as childcare like as possible whilst also keeping our company colors (same as logo). We would also like for this flyer to stand out and be appealing to the recipient as this flyer is to gain potential clients, with emphasis on the HLTAID004 Course
Updates

Just need to update the qualifications: In the design brief I mentioned that the course; HLTAID001 Provide CPR and Asthma & Anaphyalxis.. Can this please be changed to HLTAID001 Provide Cardiopulmonary Resuscitation (CPR) And 22024VIC Course in emergency management of asthma in the workplace And 22099VIC Course in First Aid Management of Anaphylaxis (They are all singular courses) Apoligies!

Target Market(s)

Childcare centres, Out of school hours providers, pre-schools

Industry/Entity Type

Childcare

Font styles to use
Decorative

Colors
ffcf3e
f37123
faa54b

Requirements
Must have
• Company Logo
phone number
website
email
Registered Training Organisation
TOID: 47318

```html
<!DOCTYPE html>
<html lang="en">
<head>
<meta charset="utf-8">
<title>Spring Special – Ferngate Skills Academy</title>
<link href="https://fonts.googleapis.com/css2?family=Arimo:wght@400;700&family=Chewy&family=Luckiest+Guy&display=swap" rel="stylesheet">
<style>
  :root {
    --orange-deep: #f37123;
    --orange-light: #faa54b;
    --yellow: #ffcf3e;
    --white: #ffffff;
    --ink-grey: #5a5a5a;
    --shadow-brown: #7a2e08;
    --photo-warm: #f5b47a;
    --photo-skin: #e9c3a5;
    --kids-sky: #fde3c4;
    --kids-tone: #f9c894;
    --card-blue: #2f4fa6;
  }
  html, body {
    margin: 0;
    padding: 0;
    width: 992px;
    height: 1200px;
    overflow: hidden;
    background: var(--white);
  }
  .flyer {
    position: relative;
    width: 992px;
    height: 1200px;
    overflow: hidden;
    background: var(--white);
    font-family: "Arimo", Arial, sans-serif;
  }
  .flyer-backdrop, .hero-photo {
    position: absolute;
    left: 0;
    top: 0;
  }
  .gift-card {
    position: absolute;
    left: 162px;
    top: 89px;
    width: 124px;
    height: 84px;
    border-radius: 8px;
    background: linear-gradient(135deg, var(--card-blue), #4466c4);
    transform: rotate(-4deg);
  }
  .promo-headline {
    position: absolute;
    left: 96px;
    top: 206px;
    margin: 0;
    font-family: "Luckiest Guy", Impact, "Arial Black", sans-serif;
    font-weight: 400;
    color: var(--white);
    text-shadow: 3px 3px 0 var(--shadow-brown);
    line-height: 1;
    letter-spacing: 0.5px;
    text-transform: uppercase;
  }
  .promo-line { display: block; }
  .promo-line--offer { font-size: 30px; }
  .promo-line--offer .promo-big { font-size: 54px; }
  .promo-line--card { font-size: 31px; margin-top: 2px; }
  .promo-line--discount { font-size: 30px; margin-top: 18px; }
  .promo-line--discount .promo-big { font-size: 58px; }
  .promo-line--session { font-size: 29px; margin-top: 2px; }
  .conditions {
    position: absolute;
    left: 152px;
    top: 432px;
    margin: 0;
    font-size: 22px;
    color: var(--yellow);
  }
  .season-title {
    position: absolute;
    left: 410px;
    top: 470px;
    margin: 0;
    font-family: "Chewy", "Comic Sans MS", cursive;
    font-weight: 400;
    color: var(--yellow);
    text-shadow: 4px 4px 0 var(--shadow-brown);
    line-height: 0.95;
    transform: rotate(-6deg);
    transform-origin: left top;
  }
  .season-title span { display: block; font-size: 86px; }
  .season-title .season-second { margin-left: 170px; margin-top: -4px; }
  .kids-photo {
    position: absolute;
    left: 70px;
    top: 468px;
    width: 360px;
    height: 222px;
    border-radius: 28px;
    background: linear-gradient(180deg, var(--kids-sky) 0%, var(--kids-tone) 100%);
  }
  .course-section {
    position: absolute;
    left: 109px;
    top: 700px;
    width: 860px;
  }
  .course-title {
    margin: 0 0 12px 345px;
    font-size: 46px;
    font-weight: 400;
    line-height: 1.1;
    color: var(--orange-deep);
  }
  .course-list {
    list-style: none;
    margin: 0;
    padding: 0;
  }
  .course-item {
    font-size: 18px;
    line-height: 1.2;
    color: var(--ink-grey);
    margin-bottom: 9px;
    white-space: nowrap;
  }
  .course-code {
    font-size: 24px;
    color: var(--orange-deep);
  }
  .course-item--featured {
    font-weight: 700;
    color: var(--orange-deep);
  }
  .course-item--featured .course-code { font-weight: 700; }
  .course-tag {
    display: inline-block;
    margin-right: 8px;
    padding: 2px 8px;
    border-radius: 4px;
    background: var(--yellow);
    color: var(--shadow-brown);
    font-size: 15px;
    font-weight: 700;
    vertical-align: 3px;
  }
  .contact {
    position: absolute;
    left: 60px;
    top: 958px;
    width: 680px;
    text-align: center;
    color: var(--orange-deep);
  }
  .contact p { margin: 0; }
  .contact-phone {
    font-size: 46px;
    font-weight: 700;
    line-height: 1;
    display: flex;
    align-items: center;
    justify-content: center;
    gap: 14px;
  }
  .contact-email {
    font-size: 24px;
    font-weight: 700;
    margin-top: 18px;
    display: flex;
    align-items: center;
    justify-content: center;
    gap: 12px;
  }
  .contact-web {
    font-size: 30px;
    font-weight: 700;
    margin-top: 12px;
  }
  .contact-rto {
    font-size: 21px;
    margin-top: 16px;
  }
  .icon { fill: var(--orange-deep); flex: none; }
  .brand {
    position: absolute;
    left: 750px;
    top: 940px;
    width: 210px;
    text-align: center;
  }
  .brand-dot {
    width: 84px;
    height: 84px;
    margin: 0 auto 18px;
    border-radius: 50%;
    background: var(--orange-deep);
  }
  .brand-name {
    margin: 0;
    font-size: 26px;
    font-weight: 400;
    line-height: 1.15;
    color: var(--ink-grey);
  }
</style>
</head>
<body>
<main class="flyer">
  <svg class="flyer-backdrop" width="992" height="1200" viewBox="0 0 992 1200" aria-hidden="true">
    <rect x="0" y="0" width="992" height="700" fill="#faa54b"/>
    <path d="M0,190 C180,150 350,80 400,0 L992,0 L992,663 C700,640 300,560 0,340 Z" fill="#f37123"/>
    <path d="M0,340 C300,560 700,640 992,663 L992,1200 L0,1200 Z" fill="#ffffff"/>
  </svg>

  <svg class="hero-photo" width="992" height="600" viewBox="0 0 992 600" role="img" aria-label="Photo of a smiling carer applying a bandage to a young girl's knee">
    <defs>
      <linearGradient id="photoTone" x1="0" y1="0" x2="1" y2="1">
        <stop offset="0" stop-color="#e9c3a5"/>
        <stop offset="1" stop-color="#f5b47a"/>
      </linearGradient>
    </defs>
    <path d="M470,0 C420,200 470,470 700,540 L992,560 L992,0 Z" fill="url(#photoTone)"/>
  </svg>

  <div class="gift-card" role="img" aria-label="LUMBO gift card"></div>

  <h1 class="promo-headline">
    <span class="promo-line promo-line--offer">Offer a <span class="promo-big">$50</span></span>
    <span class="promo-line promo-line--card">LUMBO Gift Card</span>
    <span class="promo-line promo-line--discount">&amp; <span class="promo-big">50%</span> of your</span>
    <span class="promo-line promo-line--session">Second Training Session</span>
  </h1>
  <p class="conditions">Conditions Apply</p>

  <div class="kids-photo" role="img" aria-label="Photo of four cheering children jumping with arms raised"></div>

  <h2 class="season-title"><span>Spring</span><span class="season-second">Special</span></h2>

  <section class="course-section">
    <h3 class="course-title">Our Course</h3>
    <ul class="course-list">
      <li class="course-item course-item--featured"><span class="course-tag">NEW</span><span class="course-code">HLTAID004</span> Provide an emergency first aid response in an education and care setting</li>
      <li class="course-item"><span class="course-code">HLTAID003</span> Provide First Aid</li>
      <li class="course-item"><span class="course-code">HLTAID001</span> Provide Cardiopulmonary Resuscitation (CPR)</li>
      <li class="course-item"><span class="course-code">22024VIC</span> Course in emergency management of asthma in the workplace</li>
      <li class="course-item"><span class="course-code">22099VIC</span> Course in First Aid Management of Anaphylaxis</li>
    </ul>
  </section>

  <section class="contact">
    <p class="contact-phone">
      <svg class="icon" width="34" height="34" viewBox="0 0 24 24" aria-hidden="true"><path d="M6.6 10.8a15.1 15.1 0 0 0 6.6 6.6l2.2-2.2a1 1 0 0 1 1-.25 11.4 11.4 0 0 0 3.6.57 1 1 0 0 1 1 1V20a1 1 0 0 1-1 1A17 17 0 0 1 3 4a1 1 0 0 1 1-1h3.5a1 1 0 0 1 1 1c0 1.25.2 2.45.57 3.57a1 1 0 0 1-.25 1z"/></svg>
      (03) 5550 1274
    </p>
    <p class="contact-email">
      <svg class="icon" width="26" height="20" viewBox="0 0 28 22" aria-hidden="true"><rect x="0" y="0" width="28" height="22" rx="2"/><path d="M2 3 L14 12 L26 3" fill="none" stroke="#ffffff" stroke-width="2"/></svg>
      maraflint@ferngateskillsacademy.com.au
    </p>
    <p class="contact-web">www.ferngateskillsacademy.com.au</p>
    <p class="contact-rto">Registered Training Organisation TOID: 47318</p>
  </section>

  <div class="brand">
    <div class="brand-dot"></div>
    <p class="brand-name">Ferngate<br>Skills Academy</p>
  </div>
</main>
</body>
</html>
```